Company Website for Zorvel Analytics, an open source data analytics company focused on relationship and li

I need a company/brand website for our new startup, Zorvel Analytics LLC. We are a company focused on using life pattern analysis techniques, looking at relationships and how relationships, attributes, and activity cluster to infer aggregate information about individuals and groups. Our focus is on improving the digital advertising market.

We have a company logo which I will upload shortly.

Target Market(s)

Digital Advertising

Number of Pages Required

3 page

Font styles to use
Sans Serif

Requirements
Must have
• An main page, about us, contact page.
Nice to have
• Zorvel Analytics relies on state of the art analytics applied to a the digital marketing space. While it is heavy in science, we also understand the art of influence. The website should have a scientific edge but also a flair that illustrates our focus on applying the hard science and analytics to influencing the behavior of people.

```html
<!DOCTYPE html>
<html lang="en">
<head>
<meta charset="utf-8">
<title>Zorvel Analytics — Know More About Your Customers</title>
<link rel="stylesheet" href="https://fonts.googleapis.com/css2?family=Jost:wght@400;500;600&display=swap">
<style>
  :root {
    --sky-top: #2a7cae;
    --sky-mid: #5b9dc8;
    --sky-low: #a9c6d9;
    --sand: #d8b894;
    --ground: #4b5057;
    --ground-dark: #33373c;
    --accent: #f7941d;
    --white: #ffffff;
    --brand-blue: #1f5fae;
  }
  html, body {
    margin: 0;
    padding: 0;
    overflow: hidden;
  }
  body {
    width: 1200px;
    height: 750px;
    font-family: "Jost", sans-serif;
  }
  .hero {
    position: relative;
    width: 1200px;
    height: 750px;
    overflow: hidden;
  }
  .hero-photo {
    position: absolute;
    inset: 0;
    background: linear-gradient(180deg, var(--sky-top) 0%, var(--sky-mid) 45%, var(--sky-low) 86%, var(--sand) 88.5%, var(--ground) 89%, var(--ground-dark) 100%);
  }
  .hero-shape {
    position: absolute;
    inset: 0;
  }
  .site-nav {
    position: absolute;
    top: 68px;
    left: 785px;
    display: flex;
    gap: 63px;
  }
  .site-nav a {
    color: var(--white);
    text-decoration: none;
    font-size: 20px;
    font-weight: 500;
  }
  .brand-box {
    position: absolute;
    top: 0;
    right: 0;
    width: 148px;
    height: 148px;
    background: var(--white);
    display: flex;
    align-items: center;
    justify-content: center;
    gap: 6px;
  }
  .brand-mark {
    width: 10px;
    height: 10px;
    background: var(--accent);
  }
  .brand-name {
    color: var(--brand-blue);
    font-size: 13px;
    font-weight: 600;
  }
  .profile-rule {
    position: absolute;
    left: 436px;
    top: 247px;
    width: 50px;
    height: 3px;
    background: var(--accent);
  }
  .profile-notes {
    position: absolute;
    left: 436px;
    top: 268px;
    margin: 0;
    color: var(--white);
    font-size: 12px;
    line-height: 16px;
  }
  .headline {
    position: absolute;
    left: 100px;
    top: 360px;
    margin: 0;
    color: var(--white);
    font-size: 80px;
    font-weight: 500;
    line-height: 88px;
    letter-spacing: 0.5px;
  }
  .cta {
    position: absolute;
    left: 100px;
    top: 585px;
    width: 222px;
    height: 64px;
    background: var(--accent);
    color: var(--white);
    font-size: 23px;
    font-weight: 600;
    text-decoration: none;
    display: flex;
    align-items: center;
    justify-content: center;
  }
</style>
</head>
<body>
<main class="hero">
  <div class="hero-photo" role="img" aria-label="Photo of a sprinter launching forward on an asphalt road under a clear blue sky, desert dunes on the horizon"></div>
  <svg class="hero-shape" width="1200" height="750" viewBox="0 0 1200 750" aria-hidden="true">
    <polygon points="638,367 796,279 886,433 725,525" fill="var(--accent)"/>
  </svg>

  <nav class="site-nav">
    <a href="#about">About</a>
    <a href="#contacts">Contacts</a>
  </nav>

  <div class="brand-box">
    <span class="brand-mark"></span>
    <span class="brand-name">Zorvel Analytics</span>
  </div>

  <div class="profile-rule"></div>
  <p class="profile-notes">athlete,<br>24 years old,<br>has a wife,<br>in love with motorcycles</p>

  <h1 class="headline">Know More About<br>Your Customers</h1>

  <a class="cta" href="#contacts">Contact Us</a>
</main>
</body>
</html>
```